Advertising agency needs site design

You will be designing a clean (plenty of white space) and vivid (colorful) design that is for an advertising agency named Beacon Brightly. Their current web site is located at www.BeaconBrightly.net. From there you can see their services and get a feel for the company as the site stands today.
The following are direct quotes from the client:
“I want a clean look with colors of the teal blue, deep yellow (in logo) and then a good energetic orange (deep orange - rich) should bring a good feel and enthusiasm.”
“The orange can be a nice accent color, not dominant.”
“Saw two other things I like - the website fizzlarkstudio.com was pretty cool. I liked how the top banner changed colors as you moved to different tabs. I am somewhat wanting the colors I mentioned - like the blue color we use can be lighter as long as it works with the logo. - love the zing leaves site. I want quirky, creative and clean look - fun feel but slightly sophisticated to work with the medical field.”
Beacon Brightly currently focuses on the following primary industries:
• Medical / Health Care – Currently the primary industry
• Retail Industry
• Automotive Industry
• Entertainment Industry
Primary Services
• Media Planning & Buying: Web, TV, Print, Radio
• Campaign monitoring and reporting
• Commercial Production: TV & Radio
• Strategic Planning
• Market Research
• Internet Marketing: Email, SEO, Web design / development
Primary Navigation will consist of the following:
• Home
• About Us
o History
o Principal Profile (sub nav)
o Sales Team & Partners
• Clients
• Services
• Testimonials
• Contact Us
They want the web site to act as a basis for future marketing collateral so the overall feel from the web site must be capable of translating to print and other collateral. I do not currently have a clean digital version of their logo however their logo is on the web site (beaconbrightly.net)
Target Market(s)
larger companies that are purchasing air time on television and radio. Typically in the health care industry and others described above in brief.
Industry/Entity Type
Advertising
Look and feel

```html
<!DOCTYPE html>
<html lang="en">
<head>
<meta charset="utf-8">
<title>Beacon Brightly — Advertising Agency</title>
<link href="https://fonts.googleapis.com/css2?family=Questrial&family=Open+Sans:ital,wght@0,400;0,600;0,700;1,600&family=Oswald:wght@400&display=swap" rel="stylesheet">
<style>
:root{
  --teal-top:#1f6d8e;
  --teal-deep:#0b3c58;
  --teal-panel:#0c4766;
  --gold:#f9b20f;
  --gold-light:#ffd873;
  --ink:#1b1b1b;
  --panel-bg:#f3f3f3;
  --white:#ffffff;
}
*{margin:0;padding:0;box-sizing:border-box}
html,body{width:1200px;height:1102px;overflow:hidden;background:var(--white)}
body{position:relative;font-family:"Open Sans",sans-serif;color:var(--ink)}
.abs{position:absolute}

.top-band{left:0;top:0;width:1200px;height:255px;background:linear-gradient(var(--teal-top),var(--teal-deep))}
.top-stripe{left:0;top:255px;width:1200px;height:6px;background:var(--gold)}
.brand{left:180px;top:44px;display:flex;align-items:center;gap:10px;font-family:"Questrial",sans-serif;font-size:30px;color:var(--white);letter-spacing:3px}
.brand-dot{width:12px;height:12px;border-radius:50%;background:var(--gold)}

.main-nav{left:546px;top:61px;display:flex;align-items:center;font-family:"Open Sans",sans-serif;font-size:15.5px;color:var(--white)}
.main-nav a{color:var(--white);text-decoration:none;margin-right:26px}
.main-nav a.is-active{background:linear-gradient(#ffc93a,#f0a000);color:#1a1a1a;padding:2px 10px;border-radius:3px;font-weight:600;margin-right:17px;box-shadow:0 1px 2px rgba(0,0,0,.4)}

.hero{left:171px;top:89px;width:859px;height:361px;background:linear-gradient(var(--gold) 0,var(--gold) 172px,var(--teal-deep) 172px);box-shadow:0 2px 4px rgba(0,0,0,.3)}
.hero-inner{left:13px;top:12px;width:833px;height:336px;background:var(--teal-panel)}
.hero-art{left:0;top:0}
.mission-title{left:526px;top:73px;font-family:"Questrial",sans-serif;font-size:26px;letter-spacing:2px;color:var(--white)}
.mission-text{left:528px;top:131px;width:300px;font-style:italic;font-weight:600;font-size:13px;line-height:16.9px;letter-spacing:.8px;color:var(--white)}
.mission-text .q{position:absolute;left:-6px;top:-10px;font-size:34px;color:#8fa9b8;font-style:normal;line-height:1}

.side-box{left:178px;width:222px}
.side-head{height:40px;background:linear-gradient(#ffe08a,#f6b21a);border-radius:3px 3px 0 0;font-family:"Oswald",sans-serif;font-size:19px;color:var(--white);text-shadow:0 1px 2px rgba(120,70,0,.7);padding:6px 0 0 36px;letter-spacing:-.3px}
.side-body{margin:0 5px;background:linear-gradient(#fff,var(--panel-bg));border:1px solid #e2e2e2;border-top:0;padding:8px 18px 0 20px}
.side-body li{list-style:none;font-size:11.5px;letter-spacing:.8px;line-height:15.8px;padding:6px 0 6px 10px;border-bottom:1px dashed #555;position:relative}
.side-body li:last-child{border-bottom:0}
.side-body li::before{content:"";position:absolute;left:0;top:13px;width:3px;height:3px;background:#111;border-radius:50%}

.welcome{left:414px;top:473px;width:350px}
.welcome h1{font-family:"Questrial",sans-serif;font-weight:400;font-size:26.5px;letter-spacing:2.2px;margin-bottom:7px}
.welcome p{font-size:11.4px;line-height:15.8px;letter-spacing:.9px;text-align:justify;margin-bottom:15px}

.right-head{left:783px;width:247px;height:28px;background:linear-gradient(#1d6b8c,var(--teal-deep));color:var(--white);font-weight:700;font-size:14px;text-align:center;padding-top:4px;border-radius:2px 2px 0 0}
.right-body{left:788px;width:236px;background:linear-gradient(#fff,#e8e8e8);border:1px solid #e0e0e0;border-top:0}
.testimonial{top:496px;height:192px;padding:12px 8px 0 20px;font-size:11px;line-height:15.8px;text-align:justify}
.testimonial .q{position:absolute;left:6px;top:12px;font-weight:700;font-size:14px;line-height:1}
.testimonial p{margin-bottom:15.8px}
.testimonial .by{text-align:right;font-weight:600;text-decoration:underline;padding-right:14px;margin-top:-3px}
.news{top:726px;height:198px}
.news-item{padding:7px 8px 4px 8px;font-size:11px;line-height:15.8px;border-bottom:1px dashed #555}
.news-item:last-child{border-bottom:0}
.news-item a{display:block;text-align:right;color:var(--ink)}

.footer{left:0;top:940px;width:1200px;height:162px;background:linear-gradient(var(--teal-top),var(--teal-deep));border-top:3px solid var(--gold)}
.footer-line{left:0;top:1089px;width:1200px;height:2px;background:var(--gold)}
.footer-h{font-family:"Questrial",sans-serif;font-size:16px;letter-spacing:1px;color:var(--white)}
.field{background:var(--white);border:2px solid #d8d8d8;font-size:13px;color:#777;letter-spacing:1px;padding:1px 5px}
.btn{background:linear-gradient(#fff,#dcdcdc);font-weight:600;font-size:12.5px;letter-spacing:1px;text-align:center;color:#111}
.copyright{left:450px;top:969px;font-weight:600;font-size:12px;letter-spacing:1px;color:var(--white)}
.foot-brand{left:458px;top:1004px;font-family:"Questrial",sans-serif;font-size:28px;letter-spacing:3px;color:var(--white);display:flex;align-items:center;gap:9px}
</style>
</head>
<body>

<div class="abs top-band"></div>
<div class="abs top-stripe"></div>

<div class="abs brand"><span>Beacon Brightly</span><span class="brand-dot"></span></div>

<nav class="abs main-nav">
  <a class="is-active" href="#">Home</a>
  <a href="#">About Us</a>
  <a href="#">Clients Services</a>
  <a href="#">Testimonials</a>
  <a href="#" style="margin-right:0">Contact Us</a>
</nav>

<section class="abs hero">
  <div class="abs hero-inner">
    <svg class="abs hero-art" width="833" height="336" viewBox="0 0 833 336">
      <defs>
        <radialGradient id="heroGlow" cx="0.55" cy="0.45" r="0.7">
          <stop offset="0" stop-color="#6ff0ff"/>
          <stop offset="0.5" stop-color="#1cb8e0"/>
          <stop offset="1" stop-color="#0a5c88"/>
        </radialGradient>
      </defs>
      <path role="img" aria-label="Business team standing in front of a world map" d="M0 0H488C455 90 520 220 460 336H0Z" fill="url(#heroGlow)"/>
      <path d="M488 0C455 90 525 220 462 336H470C530 220 468 90 504 0Z" fill="var(--gold)"/>
    </svg>
    <h2 class="abs mission-title">Our Mission</h2>
    <p class="abs mission-text"><span class="q">“</span>&nbsp;&nbsp;&nbsp;&nbsp;&nbsp;Our Mission is to apply our experience, creative and energy to assemble and executive marketing solutions with maximum impact. Implementation of carefully designed plans is undertaken with strict regard to value and results, always striving to exceed client expectations.</p>
  </div>
</section>

<aside class="abs side-box" style="top:468px">
  <div class="side-head">PRIMARY INDUSTRIES</div>
  <ul class="side-body" style="height:135px">
    <li>Medical / Health Care</li>
    <li>Retail Industry</li>
    <li>Automotive Industry</li>
    <li>Entertainment Industry</li>
  </ul>
</aside>

<aside class="abs side-box" style="top:653px">
  <div class="side-head">PRIMARY SERVICES</div>
  <ul class="side-body" style="height:232px">
    <li>Media Planning &amp; Buying</li>
    <li>Campaign monitoring and reporting</li>
    <li>Commercial Production</li>
    <li>Strategic Planning</li>
    <li>Market Research</li>
    <li>Internet Marketing</li>
  </ul>
</aside>

<main class="abs welcome">
  <h1>Welcome To Our Website</h1>
  <p>Lorem Ipsum is simply dummy text of the printing and typesetting industry. Lorem Ipsum has been the industry's standard dummy text ever since the 1500s, when an unknown printer took a galley of type and scrambled it to make a type specimen book. It has survived not only five centuries, but also the leap into electronic typesetting, remaining essentially unchanged.</p>
  <p>Lorem Ipsum is simply dummy text of the printing and typesetting industry. Lorem Ipsum has been the industry's standard dummy text ever since the 1500s, when an unknown printer took a galley of type and scrambled it to make a type specimen book.</p>
  <p>Lorem Ipsum is simply dummy text of the printing and typesetting industry. Lorem Ipsum has been the industry's standard dummy text ever since the 1500s, when an book.</p>
</main>

<div class="abs right-head" style="top:469px">Testimonials</div>
<div class="abs right-body testimonial">
  <span class="q">“</span>
  <p>Lorem Ipsum is simply dummy text of the printing and typesetting industry. Lorem Ipsum has been the industry's standard dummy text ever sincek.</p>
  <p>It has survived not only five centuries, but also the leap into electronic typesetting, remaining essentially unchanged.</p>
  <div class="by">Happy Client ”</div>
</div>

<div class="abs right-head" style="top:698px">Latest News</div>
<div class="abs right-body news">
  <div class="news-item">27.11 Lorem Ipsum is simply dummy text of the printing and typesetting industry. <a href="#">Read More</a></div>
  <div class="news-item">27.11 Lorem Ipsum is simply dummy text of the printing and typesetting industry. <a href="#">Read More</a></div>
  <div class="news-item">27.11 Lorem Ipsum is simply dummy text of the printing and typesetting industry. <a href="#">Read More</a></div>
</div>

<footer class="abs footer"></footer>
<div class="abs footer-line"></div>

<div class="abs footer-h" style="left:177px;top:958px">Subscribe Our Newsletter</div>
<div class="abs field" style="left:173px;top:991px;width:222px;height:27px"></div>
<div class="abs btn" style="left:322px;top:1035px;width:71px;height:26px;padding-top:5px">Subscribe</div>

<div class="abs copyright">Copyright ©2011 all rights reserved</div>
<div class="abs foot-brand"><span>Beacon Brightly</span><span class="brand-dot"></span></div>

<div class="abs footer-h" style="left:736px;top:961px">Contact Us</div>
<div class="abs field" style="left:737px;top:990px;width:132px;height:22px">Name</div>
<div class="abs field" style="left:737px;top:1018px;width:132px;height:21px">Email</div>
<div class="abs field" style="left:874px;top:990px;width:156px;height:49px">Message</div>
<div class="abs btn" style="left:958px;top:1044px;width:72px;height:26px;padding-top:4px;font-size:14px">Send</div>

</body>
</html>
```